Campaign Flyer for a local election

Black and white election flyer

See information below to be included:

Re-elect Dorian
Experienced Willows Board Member
Experienced NYC Principal
Experienced leader

One Year Board Accomplishments:
-Installed New Park Lights (Bollards)
-Red Brick Road Repair Project
-Established Closer Ties with Our local precinct to frequently monitor the community with directed security patrols. Requested an increased police presence.
-Met with the 62nd Precinct Officials & Assemblywoman, Marla Quintrell to discuss our security issues
- Focused on maintenance of streetlights to make brighter streets
-Negotiated Contract & Hired Our New Landscaper, Oakhollow Landscapers
-Major Homeowner Shrub Replacement Project
- Addressing Standing Water in our Park (Installed French Drain)
- Replaced and upgraded all 5 outdoor circuit breaker panels
-Write monthly community newsletters
-Sewer cleaning project (had all community catch basins cleaned)
-Carefully overseeing our new school project. Coordinating with the sponsor and the school directors
-Delivered a very healthy budget to the community
-Works closely with our committees
-Events: Zoo event, Petting Zoo, Outdoor Movie Night, Egg Hunt

It is my intent to seek re-election.
(Photo) Dorian Lindqvist
-Dedicated to improving our community
-Hard-working…He gets thing done!
-Trustworthy

. .

Please note, I am submitting new information under accomplishments. The list of accomplishments should be in the same sequence, starting with: Met with the 62nd Precinct....
Please carefully review.
----------------------------------------------------------------------------------------------------------------------------------------------------------------

Re-elect Dorian
Experienced NYC Principal
Experienced leader

Last Year’s Board Accomplishments:

-Met with the 62nd Precinct Officials & Assemblywoman, Marla Quintrell, to discuss our security issues. Requested increased police presence.
-Established a strong partnership with the 62nd precinct to frequently monitor the community with directed security patrols.
-Replaced all new park lights (Bollards) to make the park brighter
- Focused on maintenance of streetlights to make streets brighter
-‘Fixing Our Streets Project’ (Repaired all cracked/missing red bricks)
-Homeowner Shrub Replacement Project (Replaced hundreds of bushes)
- I write the monthly community newsletter
-Carefully overseeing our new school project. Coordinating with the sponsor and the school director
-Monitoring C of O’s and homeowners Insurance

(Photo) Dorian Lindqvist
-Hard-working! I get things done!
-Trustworthy

. .

Re-elect Dorian
Experienced NYC Principal
Experienced leader

(Photo) Dorian Lindqvist
-Trustworthy

. .

Target Market(s)

A Community electing a Board Member

Industry/Entity Type

residential election

Requirements
Must have
• all black, white and grey print. Flyers will not be printed in color
Nice to have
• See the information in the attachment below containing all my accomplishments
Should not have
• color

```html
<!DOCTYPE html>
<html lang="en">
<head>
<meta charset="utf-8">
<title>Re-elect Dorian – Campaign Postcard</title>
<link rel="stylesheet" href="https://fonts.googleapis.com/css2?family=Fraunces:opsz,wght@144,800;144,900&family=Jost:wght@400;500&family=Roboto:wght@400&display=swap">
<style>
  :root {
    --backdrop: #5e5e5e;
    --panel-dark: #545454;
    --paper: #ffffff;
    --ink: #1c1c1c;
    --ink-soft: #2e2e2e;
    --grey-name: #a8a8a8;
    --line: #6a6a6a;
    --photo-dark: #3a3a3a;
    --photo-light: #d8d8d8;
  }
  * { box-sizing: border-box; margin: 0; padding: 0; }
  html, body { width: 863px; height: 1200px; overflow: hidden; }
  body { background: var(--backdrop); font-family: "Jost", sans-serif; position: relative; }

  .postcard {
    position: absolute; left: 105px; width: 654px; height: 436px;
    background: var(--paper); overflow: hidden;
  }
  .postcard--front { top: 90px; }
  .postcard--back { top: 616px; }

  /* Front: left panel */
  .candidate-panel {
    position: absolute; left: 0; top: 0; width: 329px; height: 100%;
    background: var(--panel-dark); text-align: center;
  }
  .headline {
    font-family: "Fraunces", serif; font-weight: 800; line-height: 0.98;
    position: absolute; left: 0; right: 0; top: 14px; font-size: 52px;
    letter-spacing: -0.5px;
  }
  .headline .line-white { color: var(--paper); display: block; }
  .headline .line-grey { color: var(--grey-name); display: block; }
  .portrait-shield { position: absolute; left: 74px; top: 140px; width: 181px; height: 212px; }
  .credentials {
    position: absolute; left: 0; right: 0; top: 368px;
    color: var(--paper); font-size: 11.4px; line-height: 14.6px; text-transform: uppercase;
  }

  /* Front: accomplishments */
  .accomplishments { position: absolute; left: 340px; top: 30px; right: 12px; }
  .accomplishments h2 {
    font-family: "Jost", sans-serif; font-weight: 500; font-size: 15.2px;
    color: var(--ink); letter-spacing: 0.1px; margin-bottom: 12px;
  }
  .check-list { list-style: none; display: flex; flex-direction: column; gap: 5.3px; }
  .check-list li {
    position: relative; padding-left: 11.5px;
    font-size: 9.6px; line-height: 12.8px; color: var(--ink-soft);
  }
  .check-list li::before {
    content: ""; position: absolute; left: 0; top: 3px; width: 7px; height: 7px;
    border-radius: 50%; background: var(--ink);
  }
  .check-list li::after {
    content: ""; position: absolute; left: 2.2px; top: 4.4px; width: 2.6px; height: 1.5px;
    border-left: 1.1px solid var(--paper); border-bottom: 1.1px solid var(--paper);
    transform: rotate(-45deg);
  }

  /* Back */
  .mail-name {
    position: absolute; left: 30px; top: 12px;
    font-family: "Fraunces", serif; font-weight: 800; font-size: 54px; line-height: 0.98;
    letter-spacing: -0.5px;
  }
  .mail-name .first { color: var(--ink); display: block; }
  .mail-name .last { color: var(--grey-name); display: block; }
  .intent {
    position: absolute; left: 35px; top: 144px;
    font-weight: 500; font-size: 15.2px; color: var(--ink); text-transform: uppercase;
  }
  .check-list--short { position: absolute; left: 35px; top: 175px; gap: 5.3px; }
  .check-list--short li { font-size: 9.8px; padding-left: 13.5px; }

  .postage-indicia {
    position: absolute; left: 545px; top: 25px; width: 82px; height: 82px;
    border: 1px solid var(--line); font-family: "Roboto", sans-serif;
    font-size: 10.6px; line-height: 14.4px; text-align: center; color: var(--ink);
    padding-top: 4px;
  }
  .address-line { position: absolute; left: 350px; width: 277px; height: 1px; background: var(--line); }
  .address-line:nth-of-type(1) { top: 146px; }
  .address-line:nth-of-type(2) { top: 182px; }
  .address-line:nth-of-type(3) { top: 218px; }

  .scenery {
    position: absolute; left: 0; bottom: 0; width: 100%; height: 194px;
    background: linear-gradient(180deg, #e9e9e9 0%, #8d8d8d 18%, #b9b9b9 40%, #7a7a7a 70%, #5a5a5a 100%);
  }
</style>
</head>
<body>

<section class="postcard postcard--front">
  <div class="candidate-panel">
    <h1 class="headline">
      <span class="line-white">Re-elect</span>
      <span class="line-grey">Dorian</span>
    </h1>
    <svg class="portrait-shield" viewBox="0 0 181 212" role="img" aria-label="Portrait of the candidate in front of a waving American flag, inside a shield frame">
      <defs>
        <radialGradient id="shieldGlow" cx="50%" cy="45%" r="60%">
          <stop offset="70%" stop-color="#ffffff" stop-opacity="0.35"/>
          <stop offset="100%" stop-color="#ffffff" stop-opacity="0"/>
        </radialGradient>
        <linearGradient id="portraitTone" x1="0" y1="0" x2="0" y2="1">
          <stop offset="0%" stop-color="#d0d0d0"/>
          <stop offset="100%" stop-color="#3c3c3c"/>
        </linearGradient>
      </defs>
      <ellipse cx="90.5" cy="100" rx="96" ry="112" fill="url(#shieldGlow)"/>
      <path d="M6 12 Q90 -4 175 12 L175 90 Q170 160 90.5 206 Q11 160 6 90 Z" fill="var(--photo-dark)"/>
      <path d="M17 22 Q90 10 164 22 L164 92 Q158 150 90.5 190 Q23 150 17 92 Z" fill="url(#portraitTone)"/>
    </svg>
    <p class="credentials">
      Experienced Willows Board Member<br>
      Experienced NYC Principal<br>
      Experienced Leader
    </p>
  </div>

  <div class="accomplishments">
    <h2>ONE YEAR BOARD ACCOMPLISHMENTS:</h2>
    <ul class="check-list">
      <li>Installed New Park Lights (Bollards)</li>
      <li>Red Brick Road Repair Project</li>
      <li>Established Closer Ties with Our local precinct to frequently<br>monitor the community with directed security patrols.</li>
      <li>Requested an increased police presence.</li>
      <li>Met with the 62nd Precinct Officials &amp; Assembly woman,<br>Marla Quintrell to discuss our security issues</li>
      <li>Focused on maintenance of streetlights to make brighter streets</li>
      <li>Negotiated Contract &amp; Hired Our New Landscaper,<br>Oakhollow Landscapers</li>
      <li>Major Homeowner Shrub Replacement Project</li>
      <li>Addressing Standing Water in ourPark (Installed French Drain)</li>
      <li>Replaced and upgraded all 5 outdoor circuit breaker panels</li>
      <li>Write monthly community newsletters</li>
      <li>Sewer cleaning project (had all community catch basins cleaned)</li>
      <li>Carefully overseeing our new school project. Coordinating with<br>the sponsor and the school directors</li>
      <li>Delivered a very healthy budget to the community</li>
      <li>Works closely with our committees</li>
      <li>Events: Zoo event, Petting Zoo, Outdoor Movie Night, Egg Hunt</li>
    </ul>
  </div>
</section>

<section class="postcard postcard--back">
  <h1 class="mail-name">
    <span class="first">Dorian</span>
    <span class="last">Lindqvist</span>
  </h1>
  <div class="postage-indicia">PRST STD<br>US POSTAGE<br>PAID<br>CEDARPORT NJ<br>PERMIT #129</div>
  <span class="address-line"></span>
  <span class="address-line"></span>
  <span class="address-line"></span>
  <p class="intent">It is my intent to seek re-election.</p>
  <ul class="check-list check-list--short">
    <li>Dedicated to improving our community</li>
    <li>Hard-working…He gets thing done!</li>
    <li>Trustworthy</li>
  </ul>
  <div class="scenery" role="img" aria-label="Beach scene with sea, jetty, white railings and dune grass"></div>
</section>

</body>
</html>
```